The 22 Keys to a Smooth Home Loan or the 22 things that will derail your transaction and how to prevent them.

I am looking to do a series of 4 to 5 e-books that should have a consistent format and theme

The first of these should be entitled, "The 22 Keys to a Smooth Home Loan" That is similar in style to the attached e-book.
The attached e-book is pretty much the style that I am looking for, The same format can be followed. I have attached a black and white head shot image for the head shot areas that appears on page two of the attached e-book. I have also attached my company logo.
Please feel free to use the same or similar colors in my logo for the lay-out of the e-book. However please do not feel limited to those colors. - Feel free to use your imagination.

The content can be found here.

http://www.danthelendingguy.example/loan-advice.php

For the final “About” page of the e-book - Please entitle it… About Dan the Lending Guy.
The content for the last page can be found in the attached document - Dan Holloway bio2

The first page is where the creativity come in

Requirements
Must have
• Note that this project is for one e-book - However, once the designer and format is chosen the remainder of the projects will be launched

```html
<!DOCTYPE html>
<html lang="en">
<head>
<meta charset="utf-8">
<title>About Dan the Lending Guy</title>
<link rel="stylesheet" href="https://fonts.googleapis.com/css2?family=Cormorant+SC:wght@600;700&family=Jost:ital,wght@0,300;0,400;0,700;1,700&display=swap">
<style>
  :root {
    --page: #ffe68a;
    --navy: #1e2a63;
    --blue: #1f4da0;
    --quote: #3b64b6;
    --license: #8477d6;
    --ink: #253066;
  }
  * { margin: 0; padding: 0; box-sizing: border-box; }
  html, body { width: 900px; height: 1200px; overflow: hidden; background: var(--page); }
  .page {
    position: relative; width: 900px; height: 1200px; background: var(--page);
    font-family: "Jost", "Futura", sans-serif; font-weight: 300; color: var(--ink);
  }
  .content { position: absolute; left: 63px; top: 38px; width: 778px; }
  .title {
    font-family: "Cormorant SC", "Trajan Pro", serif; font-weight: 700;
    color: var(--navy); font-size: 40px; line-height: 80px; letter-spacing: 0.3px;
    white-space: nowrap; margin-bottom: 26px;
  }
  .title .name { color: var(--blue); font-size: 82px; line-height: 1; vertical-align: -6px; }
  .body-text { font-size: 17.2px; line-height: 27.5px; margin-bottom: 27px; }
  .testimonial { font-size: 26.5px; line-height: 27px; color: var(--quote); margin-bottom: 28px; }
  .testimonial q { font-weight: 700; font-style: italic; quotes: "“" "”"; }
  .testimonial .source { font-weight: 400; font-size: 22px; }
  .quotes { margin-top: 4px; margin-bottom: 2px; }
  .cta { font-weight: 700; font-size: 17.6px; line-height: 29px; color: var(--navy); margin-bottom: 22px; }
  .license-note { font-weight: 700; font-size: 17.2px; color: var(--license); margin-bottom: 30px; }
  .signature { font-size: 19px; line-height: 26px; color: var(--navy); }
  .signature .sc { font-family: "Cormorant SC", serif; font-weight: 700; font-size: 21px; }
  .signature .nick { color: var(--blue); font-weight: 300; }
  .signature .site { font-weight: 700; }
  .footer {
    position: absolute; top: 1101px; left: 63px; display: flex; align-items: center; height: 36px;
    font-family: "Cormorant SC", serif; font-weight: 700; color: var(--blue); font-size: 16.2px;
  }
  .brand { font-family: "Jost", sans-serif; font-weight: 700; font-size: 17px; color: var(--navy); width: 116px; line-height: 17px; }
  .divider { width: 2px; height: 34px; background: var(--navy); margin: 0 12px 0 8px; }
  .footer .series .num { font-size: 20px; }
  .footer .licence { margin-left: 50px; color: var(--navy); }
  .footer .licence span { color: var(--blue); }
</style>
</head>
<body>
<main class="page">
  <div class="content">
    <h1 class="title">About <span class="name">Dan</span> the Lending Guy</h1>

    <p class="body-text">Here’s all what you need to know about the mortgage industry today: One large lender is promoting a tool that doesn’t require you to interact with a human to make one of the biggest financial decisions of your life.</p>
    <p class="body-text">I believe you deserve better. And I’ve spent nearly 20 years providing my clients with the guidance they need so they don’t just get a loan — they get the right loan.</p>
    <p class="body-text">You see, the mortgage process isn’t quite as simple as the ads make it seem. It takes knowledge and experience to navigate, particularly in a competitive real-estate market, where the right combination of speed and expertise can make the difference between a successful offer and losing out on your dream home.</p>
    <p class="body-text">My clients, many of whom are first-time homebuyers or have run into resistance from other lenders, always know where they stand in that complex process. That’s because I take the time to explain their options, so they can make an informed, confident decision. And most of them, like the clients below, would even say that I’m an advisor and advocate first, and a mortgage professional second.</p>

    <div class="quotes">
      <p class="testimonial"><q>I felt that Dan really cared for me, rather than seeing the whole process as just another transaction.</q> <span class="source">Neighborly comment</span></p>
      <p class="testimonial"><q>Dan did a fantastic job of seeing me through the entire process, from ‘newbie’ to homeowner.</q> <span class="source">Neighborly comment</span></p>
    </div>

    <p class="body-text">I ’m still in contact continue to be a resource with a number for many of those my past clients, often years after they purchased or refinanced their homes. They come to me because they know I provide a level of personal service uncommon in this industry. They come to me because they know I care. And they come to me because they know I have the willingness, and the knowledge, to help.</p>

    <p class="cta">I’d love to help you — whether you’re buying, refinancing or just weighing your options. Email me or give me a call today.</p>

    <p class="license-note">Lender License Lookup, http://www.lenderlicenselookup.example/ MLO #204817</p>

    <div class="signature">
      <div><span class="sc">Dan</span> <span class="nick">“the lending guy”</span> <span class="sc">Holloway</span></div>
      <div class="site">www.danthelendingguy.example</div>
      <div>Tel: (206) 555-0148</div>
    </div>
  </div>

  <footer class="footer">
    <div class="brand">Evergreen First Lending</div>
    <div class="divider"></div>
    <div class="series">The <span class="num">22</span> Keys to a Smooth Home Loan</div>
    <div class="licence">Licence <span>MLO#204817</span></div>
  </footer>
</main>
</body>
</html>
```